Flyer Design Project

We are a mortgage company Bellwick Lending Corp. that will be looking to mail out these flyers to promote Reverse Mortgages. Some clip art of Seniors (Happy Smile having a good time) Our phone number on the flyer in a few places 888-517-2604
Text: No Celebrity Endorsers or talking heads here
Solutions for seniors... Stop worrying Start Living
Say Goodby to monthly payments with a reverse mortgage
The Loan That Pays You
Secure Your Retirement With A Reverse Mortgage
QDB Goverment Insured
Retain Complete ownership of your Home
Save and Effective Financial Tool
Pay Off Credit cards Elimanate Mortgage payments improve your home or lifestyle
No Credit score or income requirements
Faceing a foreclosure a reverse mortgage can help
Is a reverse mortgage right for you? Get the facts from a qualified reverse mortgage originator
The text above does not have to be in that order
I am having trouble with my Logo so i am getting a new file and will be able to upload it to the flyer shortly just leave room for it
Seniors over the age of 62
Financial

```html
<!DOCTYPE html>
<html lang="en">
<head>
<meta charset="utf-8">
<title>Bellwick Lending Corp. – Reverse Mortgage Flyer</title>
<link rel="stylesheet" href="https://fonts.googleapis.com/css2?family=Oswald:wght@600;700&family=Open+Sans:wght@400;600;700&display=swap">
<style>
  :root {
    --page-bg: #ececec;
    --frame-blue: #4a76b6;
    --paper: #ffffff;
    --head-blue: #3c6bb3;
    --live-green: #3f9636;
    --body-grey: #4d4d4d;
    --rule-green: #dfeadc;
    --stop-red: #e0242a;
    --stop-red-light: #f4645f;
  }
  * { margin: 0; padding: 0; box-sizing: border-box; }
  html, body { width: 1200px; height: 848px; overflow: hidden; }
  body { background: var(--page-bg); position: relative; font-family: "Open Sans", Arial, sans-serif; }

  .flyer {
    position: absolute; left: 368px; top: 79px;
    width: 464px; height: 657px;
    background: var(--paper);
    border: 8px solid var(--frame-blue);
    overflow: hidden;
  }
  .seniors-photo {
    position: absolute; left: 0; top: 0; width: 100%; height: 186px;
    background: linear-gradient(180deg, #ffffff 0%, #f7ece4 28%, #d9b39a 55%, #a9b8d8 82%, #e7ecf6 100%);
  }
  .home-scene {
    position: absolute; left: 0; top: 182px; width: 100%; height: 300px;
    background:
      linear-gradient(180deg, rgba(255,255,255,0) 70%, #ffffff 100%),
      linear-gradient(180deg, #dbe8f5 0%, #eef3f8 30%, #dfe2e4 55%, #cfd3d3 75%, #e9ecea 90%);
  }
  .content-frame {
    position: absolute; left: 20px; top: 204px; width: 409px; height: 424px;
    border: 1.5px solid var(--rule-green);
  }
  .line {
    position: absolute; left: 0; width: 100%;
    text-align: center; white-space: nowrap;
  }
  .headline {
    font-family: "Oswald", "Arial Narrow", sans-serif; font-weight: 700;
    text-transform: uppercase; color: var(--head-blue);
    transform-origin: center; letter-spacing: -0.2px;
  }
  .tagline { top: 219px; font-size: 15px; line-height: 18px; font-weight: 600; transform: scaleY(1.12); }
  .title-main { top: 236px; font-size: 35px; line-height: 40px; transform: scaleY(1.2); }
  .start-living { top: 402px; font-size: 24px; line-height: 30px; color: var(--live-green); transform: scaleY(1.15); }
  .goodbye { top: 436px; font-size: 12.5px; line-height: 16px; color: var(--live-green); font-weight: 600; transform: scaleY(1.12); }
  .loan-pays { top: 454px; font-size: 24px; line-height: 30px; transform: scaleY(1.15); }
  .secure { top: 485px; font-size: 15px; line-height: 18px; font-weight: 600; transform: scaleY(1.1); }

  .stop-sign { position: absolute; left: 175px; top: 283px; width: 114px; height: 114px; }

  .benefits {
    position: absolute; left: 0; top: 512px; width: 100%;
    text-align: center; color: var(--body-grey);
    font-size: 10.2px; line-height: 13.3px;
  }
  .benefits .insured { font-size: 12.5px; font-weight: 700; line-height: 16px; color: #555; }
  .cta {
    position: absolute; left: 0; top: 597px; width: 100%;
    text-align: center; color: var(--head-blue);
    font-size: 10.2px; line-height: 14.5px; font-weight: 700;
  }
</style>
</head>
<body>
  <main class="flyer">
    <div class="seniors-photo" role="img" aria-label="Photo of a group of smiling senior men and women holding a blank sign"></div>
    <div class="home-scene" role="img" aria-label="Photo of a white suburban house under a pale blue sky"></div>
    <div class="content-frame"></div>

    <p class="line headline tagline">No Celebrity Endorsers or Talking Heads Here</p>
    <h1 class="line headline title-main">Solutions for Seniors</h1>

    <svg class="stop-sign" viewBox="0 0 114 114" aria-label="Stop worrying">
      <defs>
        <linearGradient id="stopFill" x1="0" y1="0" x2="0" y2="1">
          <stop offset="0" stop-color="#f4645f"/>
          <stop offset="0.5" stop-color="#e0242a"/>
          <stop offset="1" stop-color="#b8161c"/>
        </linearGradient>
      </defs>
      <polygon points="33.4,1 80.6,1 113,33.4 113,80.6 80.6,113 33.4,113 1,80.6 1,33.4" fill="#ffffff" stroke="#d4d4d4" stroke-width="1"/>
      <polygon points="35.5,6 78.5,6 108,35.5 108,78.5 78.5,108 35.5,108 6,78.5 6,35.5" fill="url(#stopFill)"/>
      <text x="57" y="49" text-anchor="middle" font-family="Oswald, Arial Narrow, sans-serif" font-weight="700" font-size="31" fill="#ffffff">STOP</text>
      <text x="57" y="73" text-anchor="middle" font-family="Oswald, Arial Narrow, sans-serif" font-weight="700" font-size="19" fill="#ffffff">WORRYING</text>
      <rect x="23" y="82" width="68" height="6" fill="#ffffff"/>
    </svg>

    <p class="line headline start-living">Start Living</p>
    <p class="line headline goodbye">Say Goodby to Monthly Payments with a Reverse Mortgage</p>
    <h2 class="line headline loan-pays">The Loan That Pays You</h2>
    <p class="line headline secure">Secure Your Retirement with a Reverse Mortgage</p>

    <div class="benefits">
      <p class="insured">QDB Goverment Insured</p>
      <p>Retain Complete ownership of your Home</p>
      <p>Save and Effective Financial Tool</p>
      <p>Pay Off Credit cards Elimanate Mortgage payments improve your home or lifestyle</p>
      <p>No Credit score or income requirements</p>
      <p>Faceing a foreclosure a reverse mortgage can help</p>
    </div>

    <div class="cta">
      <p>Is a reverse mortgage right for you?</p>
      <p>Get the facts from a qualified reverse mortgage originator</p>
    </div>
  </main>
</body>
</html>
```